KLR Lending Website

Need a web site designed for a Professional Mortgage company along the lines of the draft site www.klrlending-demo.com.au

The main purpose of the site is to provide a professional image of the company and capture email address's and send out simple messages. ie "INTEREST RATE SPECIAL 4.5% FOR THE MONTH OF JUNE" or whatever...basically short punchy messages to hook people.

The content is important but a lot of that can be provided by links to our lender panel, several of which have been set up.

Most people will want to know current interest rates, and how much they can borrow along with what it will cost. There are various calculators embedded in the lenders sites such as "Repayment Calculators" Borrow Capacity Calculators" Stamp Duty Calculators"

These would be nice to have on site, but if to costly or difficult to start the links can suffice.

The site will need to be updated/amended regularily.

Example "Interest Rate Special" or "Current Special Offer" sections would be required and would need to be easyily editable and in fact would need to be able to switch them off if there is no special running.

Target Market(s)

Target market is a broad spectrum of people from young couple buying first home to older couples investing.

Industry/Entity Type

It Company

Requirements
Must have
• email capture, preferably need to enter email to enter site.

```html
<!DOCTYPE html>
<html lang="en">
<head>
<meta charset="utf-8">
<title>KLR Lending Services</title>
<link href="https://fonts.googleapis.com/css2?family=Cabin:ital,wght@0,400;0,500;1,400&family=Roboto+Condensed:wght@400&display=swap" rel="stylesheet">
<style>
:root{
  --bg:#000;
  --panel:#1b1b1b;
  --accent:#c9412c;
  --accent-text:#d9462f;
  --white:#fff;
  --muted:#9a9a9a;
  --body:#a8a8a8;
  --nav:#b5b5b5;
  --btn:#2a2a2a;
  --rule:#2e2e2e;
}
*{margin:0;padding:0;box-sizing:border-box}
html,body{width:1200px;height:1189px;overflow:hidden;background:var(--bg)}
body{position:relative;font-family:Arial,Helvetica,sans-serif;color:var(--body)}
.abs{position:absolute}
.heading{font-family:"Roboto Condensed",sans-serif;color:var(--white);text-transform:uppercase;font-weight:400;letter-spacing:-.2px}
.brand{left:169px;top:28px;width:190px;font-family:Cabin,sans-serif;font-size:22px;line-height:30px;color:var(--white);text-align:center}
.mailing{left:851px;top:25px;width:144px;height:27px;background:var(--accent);color:var(--white);font-family:Cabin,sans-serif;font-size:12px;line-height:27px;text-align:center;border-radius:2px}
.nav{top:73px;font-family:Cabin,sans-serif;font-size:12px;color:var(--nav)}
.hero{left:169px;top:117px;width:828px;height:386px;background:linear-gradient(100deg,#c9c2b8 0%,#8c2a25 28%,#b9b2a6 55%,#2b2f38 75%,#1a1c22 100%)}
.slide-arrows{left:661px;top:311px;display:flex;gap:1px}
.slide-arrows span{width:19px;height:19px;background:var(--accent);display:block}
.caption{left:661px;top:330px;width:336px;height:142px;background:rgba(20,20,20,.9)}
.caption h2{position:absolute;left:22px;top:16px;font-size:21px;color:var(--accent-text)}
.caption p{position:absolute;left:22px;top:45px;width:300px;font-size:11px;line-height:19px;color:var(--muted)}
.register{position:absolute;left:23px;top:90px;width:99px;height:31px;background:var(--accent);color:var(--white);font-family:"Roboto Condensed",sans-serif;font-size:16px;line-height:31px;text-align:center}
.welcome h1{position:absolute;left:168px;top:530px;font-size:23px}
.welcome p{position:absolute;left:170px;top:563px;width:830px;font-size:10.5px;line-height:20px;color:var(--body)}
.calc{top:659px;width:406px;height:137px}
.calc-interest{left:169px;background:linear-gradient(90deg,#23272c 0%,#2e333a 55%,#545a63 75%,#1f2328 100%)}
.calc-repay{left:591px;background:linear-gradient(90deg,#22354a 0%,#3d5875 55%,#9fb4c8 85%,#6d86a1 100%)}
.calc h3{position:absolute;left:23px;top:20px;font-size:23px}
.calc p{position:absolute;left:23px;top:51px;width:260px;font-size:10.5px;line-height:20px;color:var(--white)}
.calc .click{position:absolute;left:23px;top:95px;font-family:"Roboto Condensed",sans-serif;font-size:17px;color:var(--accent-text)}
.col-title{top:834px;font-size:18px}
.thumb{top:868px;width:220px;height:93px}
.thumb-services{left:169px;background:linear-gradient(180deg,#4c8fd0 0%,#a9cdea 60%,#e9d7c3 100%)}
.thumb-partners{left:415px;background:linear-gradient(90deg,#6a5a4a 0%,#c7b8a2 40%,#efe9df 100%)}
.excerpt{top:974px;width:225px;font-family:Cabin,sans-serif;font-size:9.8px;line-height:17px;color:var(--muted)}
.more{top:1035px;width:80px;height:21px;background:var(--btn);color:#cfcfcf;font-family:Cabin,sans-serif;font-size:9.8px;line-height:21px;text-align:center}
.testi-arrows{left:975px;top:843px;display:flex;gap:7px}
.quote{font-family:Georgia,serif;font-size:38px;color:#3c3c3c;line-height:1}
.testi{left:693px;top:883px;width:285px;font-family:Cabin,sans-serif;font-size:9.8px;line-height:17px;color:var(--muted)}
.testi-name{left:693px;top:978px;font-family:Cabin,sans-serif;font-size:10.5px;color:var(--accent-text)}
.testi-date{left:693px;top:995px;font-family:Cabin,sans-serif;font-size:9.5px;font-style:italic;color:var(--muted)}
.footer-rule{left:167px;top:1087px;width:828px;height:3px;background:var(--rule)}
.footer-nav{left:174px;top:1108px;font-size:9.5px;color:#c4c4c4;display:flex;gap:0}
.footer-nav span{white-space:pre}
.copyright{left:174px;top:1134px;font-size:9.5px;color:var(--muted)}
.social{top:1113px;width:21px;height:21px;border-radius:50%;background:#4a4a4a}
</style>
</head>
<body>
<header>
  <div class="abs brand">KLR Lending<br>Services</div>
  <div class="abs mailing">Join our mailing list</div>
  <nav>
    <span class="abs nav" style="left:483px">Home</span>
    <span class="abs nav" style="left:561px">About Us</span>
    <span class="abs nav" style="left:654px">Services</span>
    <span class="abs nav" style="left:742px">Our Clients</span>
    <span class="abs nav" style="left:844px">Partners</span>
    <span class="abs nav" style="left:933px">Contact us</span>
  </nav>
</header>

<section>
  <div class="abs hero" role="img" aria-label="Photo of a young couple reviewing loan papers with a mortgage adviser outside a house"></div>
  <div class="abs slide-arrows">
    <span><svg width="19" height="19"><path d="M11 6 L7.5 9.5 L11 13" stroke="#fff" fill="none" stroke-width="1.2"/></svg></span>
    <span><svg width="19" height="19"><path d="M8 6 L11.5 9.5 L8 13" stroke="#fff" fill="none" stroke-width="1.2"/></svg></span>
  </div>
  <div class="abs caption">
    <h2 class="heading">Get Registered With Us</h2>
    <p>KLR Lending Services offers a complete range of Mortgage and Loan products...</p>
    <div class="register">REGISTER</div>
  </div>
</section>

<section class="welcome">
  <h1 class="heading">Welcome to KLR Lending Services</h1>
  <p>KLR Lending Services offers a complete range of Mortgage and Loan products to suit our individual clients needs.<br>Whether your a First Home Buyer, Up-Sizing or Down-Sizing, Refinancing, Investing or simply want a new car or equipment purchase, contact us for a no obligation assessment and get the latest information on the available products to suit you needs.</p>
</section>

<section>
  <div class="abs calc calc-interest" role="img" aria-label="Close-up of a calculator keypad">
    <h3 class="heading">Interest Calculator</h3>
    <p>KLR Lending Services offers a complete range of Mortgage and Loan products...</p>
    <span class="click">CLICK HERE</span>
  </div>
  <div class="abs calc calc-repay" role="img" aria-label="Stack of coins on a financial chart">
    <h3 class="heading">Repayment Calculators</h3>
    <p>KLR Lending Services offers a complete range of Mortgage and Loan products...</p>
    <span class="click">CLICK HERE</span>
  </div>
</section>

<section>
  <h4 class="abs heading col-title" style="left:170px">Services</h4>
  <div class="abs thumb thumb-services" role="img" aria-label="Small model house held in an open hand against the sky"></div>
  <p class="abs excerpt" style="left:170px">Standard Loan Clients - Whether your purchasing your first home, up sizing or down sizing KLR, with it's extensive range...</p>
  <div class="abs more" style="left:170px">Read More</div>

  <h4 class="abs heading col-title" style="left:416px">Partners</h4>
  <div class="abs thumb thumb-partners" role="img" aria-label="Two business people shaking hands"></div>
  <p class="abs excerpt" style="left:416px">Standard Loan Clients - Whether your purchasing your first home, up sizing or down sizing KLR, with it's extensive range...</p>
  <div class="abs more" style="left:416px">Read More</div>

  <h4 class="abs heading col-title" style="left:668px;top:836px">Testimonials</h4>
  <div class="abs testi-arrows">
    <svg width="6" height="9"><path d="M5 1 L1.5 4.5 L5 8" stroke="#777" fill="none"/></svg>
    <svg width="6" height="9"><path d="M1 1 L4.5 4.5 L1 8" stroke="#777" fill="none"/></svg>
  </div>
  <span class="abs quote" style="left:669px;top:868px">&ldquo;</span>
  <p class="abs testi">Standard Loan Clients - Whether your purchasing your first home, up sizing or down sizing KLR, with it's extensive range of quality lenders has a loan product to suit your needs. with it's extensive range of quality lenders has a loan product ...</p>
  <span class="abs quote" style="left:978px;top:945px">&rdquo;</span>
  <span class="abs testi-name">Dylan Parker</span>
  <span class="abs testi-date">Posted on 27 Oct 2013</span>
  <div class="abs more" style="left:694px">Read More</div>
</section>

<footer>
  <div class="abs footer-rule"></div>
  <div class="abs footer-nav"><span>Home      |      About Us      |      Services      |      Our Clients      |      Partners      |      Contact us</span></div>
  <div class="abs copyright">Copyrights &copy; 2013 KLR Lending Services. All rights reserved</div>
  <span class="abs social" style="left:914px"></span>
  <span class="abs social" style="left:943px"></span>
  <span class="abs social" style="left:972px"></span>
</footer>
</body>
</html>
```